Mara Lindqvist Advisory Business Cards

Hi - using the information and logo provided I require a two sided business card designed with the following information. The business card is a 'mini card' 3.5" x 1.25".

Front of card should be the logo attached but inverted (so the background is the peach colour and the logo white).

Back should have these details. If we can't fit the Instragram and Facebook part can we just put the little logos.

Mara Lindqvist

Art and Design Consultant
Dealer - Curator - Events - Styling - Creative Sourcing

P: 0438 519 207
E: mara@maralindqvistadvisory.com
W: www.maralindqvistadvisory.com
I (instagram image please): maralindqvistadvisory F (Facebook image please): MaraLindqvistAdvisor

Target Market(s)

Galleries, artists, art buyers, interior design clients, event managers, creative types

Industry/Entity Type

Business

```html
<!DOCTYPE html>
<html lang="en">
<head>
<meta charset="utf-8">
<title>Mara Lindqvist Advisory – Mini Business Card</title>
<link href="https://fonts.googleapis.com/css2?family=Tinos:wght@400&display=swap" rel="stylesheet">
<style>
  :root {
    --backdrop: #5f5048;
    --card-dark: #141414;
    --card-light: #ffffff;
    --peach: #f1b497;
    --ink: #1a1a1a;
    --mark-grey: #5d5d5d;
    --rule-dark: #3a3a3a;
    --rule-light: #d6d6d6;
    --icon: #333333;
  }
  * { margin: 0; padding: 0; box-sizing: border-box; }
  html, body {
    width: 1200px; height: 960px; overflow: hidden;
    background: var(--backdrop);
    font-family: "Tinos", "Times New Roman", serif;
  }
  .canvas { position: relative; width: 1200px; height: 960px; }
  .card { position: absolute; width: 886px; height: 316px; box-shadow: 0 18px 26px rgba(0,0,0,0.35); }
  .card--front { left: 30px; top: 62px; background: var(--card-dark); }
  .card--back { left: 288px; top: 454px; background: var(--card-light); }
  .abs { position: absolute; }

  /* Front */
  .brand-panel {
    left: 38px; top: 0; width: 322px; height: 218px;
    background: var(--card-light);
    border-radius: 0 0 16px 16px;
  }
  .brand-dot {
    left: 106px; top: 10px; width: 110px; height: 110px;
    border-radius: 50%; background: var(--peach);
  }
  .brand-name {
    left: 0; width: 322px; text-align: center; color: var(--mark-grey);
    text-transform: uppercase; line-height: 1; font-weight: 400;
  }
  .brand-name--main { top: 132px; font-size: 26px; letter-spacing: 3px; }
  .brand-name--sub { top: 170px; font-size: 19px; letter-spacing: 5px; }

  .rule-dark { height: 1px; background: var(--rule-dark); }
  .rule-dark--top { left: 378px; top: 24px; width: 472px; }
  .rule-dark--mid { left: 30px; top: 245px; width: 820px; }
  .rule-dark--low { left: 30px; top: 290px; width: 820px; }

  .person-name { left: 400px; top: 82px; font-size: 38px; color: var(--peach); line-height: 1; }
  .person-role { left: 400px; top: 120px; font-size: 21px; color: var(--peach); line-height: 1; }
  .services {
    left: 30px; top: 246px; width: 820px; height: 44px;
    display: flex; align-items: center; justify-content: center;
    font-size: 23px; color: var(--peach); white-space: nowrap;
  }

  /* Back */
  .rule-light { height: 1px; background: var(--rule-light); left: 28px; width: 830px; }
  .rule-light--top { top: 34px; }
  .rule-light--mid { top: 238px; }
  .rule-light--low { top: 288px; }

  .back-mark { left: 52px; top: 50px; width: 164px; height: 170px; text-align: center; }
  .back-mark__dot {
    width: 104px; height: 104px; border-radius: 50%;
    background: var(--peach); margin: 4px auto 12px;
  }
  .back-mark__name {
    color: var(--mark-grey); font-size: 14px; letter-spacing: 2px;
    text-transform: uppercase; line-height: 1.35;
  }

  .contact { left: 236px; font-size: 26px; color: var(--ink); line-height: 1; white-space: nowrap; }
  .contact__label { font-size: 27px; }
  .contact--phone { top: 80px; }
  .contact--email { top: 124px; }
  .contact--web { top: 164px; }

  .social {
    top: 239px; height: 49px; display: flex; align-items: center; gap: 16px;
    font-size: 24px; color: var(--ink); white-space: nowrap;
  }
  .social--first { left: 49px; }
  .social--second { left: 492px; }
  .social__square { width: 34px; height: 34px; border-radius: 3px; background: var(--icon); }
</style>
</head>
<body>
<main class="canvas">

  <section class="card card--front" aria-label="Card front">
    <div class="abs brand-panel">
      <div class="abs brand-dot"></div>
      <div class="abs brand-name brand-name--main">Mara Lindqvist</div>
      <div class="abs brand-name brand-name--sub">Advisory</div>
    </div>
    <div class="abs rule-dark rule-dark--top"></div>
    <p class="abs person-name">Mara Lindqvist</p>
    <p class="abs person-role">(Art and Design Consultant)</p>
    <div class="abs rule-dark rule-dark--mid"></div>
    <p class="abs services">Dealer | Curator | Events | Styling | Creative Sourcing</p>
    <div class="abs rule-dark rule-dark--low"></div>
  </section>

  <section class="card card--back" aria-label="Card back">
    <div class="abs rule-light rule-light--top"></div>
    <div class="abs back-mark">
      <div class="back-mark__dot"></div>
      <p class="back-mark__name">Mara Lindqvist<br>Advisory</p>
    </div>
    <p class="abs contact contact--phone"><span class="contact__label">Phone:</span> 0438 519 207</p>
    <p class="abs contact contact--email"><span class="contact__label">Email:</span> mara@maralindqvistadvisory.com</p>
    <p class="abs contact contact--web"><span class="contact__label">Web:</span> www.maralindqvistadvisory.com</p>
    <div class="abs rule-light rule-light--mid"></div>
    <div class="abs social social--first"><span class="social__square"></span>maralindqvistadvisory</div>
    <div class="abs social social--second"><span class="social__square"></span>MaraLindqvistAdvisor</div>
    <div class="abs rule-light rule-light--low"></div>
  </section>

</main>
</body>
</html>
```